Naturopath Practitioner Card Design

I am a naturopath needing a design for a business card mainly to show that I am a naturopath and have some contact details to give to prospective clients. I am open minded about the design and what is on the second side of the card whether it just be some artwork or space for details, appointment times etc. Naturopathy is the practice of natural medicine that uses a holistic approach and incorporates herbal and nutritional medicine.

Industry/Entity Type

Business

Contact Information for Business Card

Tom Welby NaturopathBHSc (Naturopathy) Member PHRA 0492 815 306 tom.welby@mailbright.com www.tomwelbynaturopathy.com.au

Requirements
Nice to have
• Would prefer some kind of original pattern/art work/logo rather than an image, not fussed if its very simple/basic
• I am open to any colour but think I would prefer a more earthy sandy clay etc type style than the greens that are commonly associated with naturopathy.
Should not have
• Don't really want to have generic stock images on it

```html
<!DOCTYPE html>
<html lang="en">
<head>
<meta charset="utf-8">
<title>Tom Welby – Naturopath Business Card</title>
<link rel="stylesheet" href="https://fonts.googleapis.com/css2?family=Nunito+Sans:wght@400;600&family=Open+Sans:wght@400;700&display=swap">
<style>
  :root {
    --page-bg: #e9ebe8;
    --forest-dark: #0f5a2c;
    --forest-mid: #1f8a48;
    --forest-light: #2a9a55;
    --lime-band: #c4e58a;
    --lime-band-edge: #a9d36a;
    --text-green: #1a7a3c;
    --card-white: #ffffff;
    --leaf-border: #e3f1e2;
    --ink: #222222;
    --rule: #333333;
  }
  * { box-sizing: border-box; margin: 0; padding: 0; }
  html, body { width: 1200px; height: 873px; overflow: hidden; }
  body {
    background: var(--page-bg);
    display: flex;
    align-items: center;
    justify-content: center;
    gap: 40px;
  }
  .card {
    position: relative;
    width: 540px;
    height: 309px;
    border-radius: 4px;
    overflow: hidden;
    box-shadow: 0 6px 18px rgba(0,0,0,.18);
  }

  /* Front side */
  .card-front { font-family: "Nunito Sans", sans-serif; }
  .front-pattern {
    position: absolute; inset: 0;
    background: radial-gradient(ellipse at 70% 60%, var(--forest-light), var(--forest-mid) 45%, var(--forest-dark) 100%);
  }
  .band {
    position: absolute;
    background: var(--lime-band);
    box-shadow: inset 0 -3px 0 var(--lime-band-edge);
    color: var(--text-green);
  }
  .band-name {
    left: 40px; top: 0;
    width: 190px; height: 190px;
    border-radius: 0 0 95px 95px;
    padding: 26px 18px 0;
  }
  .practitioner-name { font-size: 30px; font-weight: 600; line-height: 1.1; }
  .credential { font-size: 16px; line-height: 1.25; }
  .band-contact {
    right: 40px; bottom: 0;
    width: 230px; height: 190px;
    border-radius: 115px 115px 0 0;
    padding: 0 18px 22px;
    display: flex; flex-direction: column; justify-content: flex-end;
  }
  .contact-line { font-size: 18px; font-weight: 600; line-height: 1.35; }
  .contact-line.email { font-size: 15px; }

  /* Back side */
  .card-back {
    background: var(--leaf-border);
    font-family: "Open Sans", sans-serif;
    color: var(--ink);
    padding: 18px;
  }
  .reminder-box {
    position: relative;
    height: 100%;
    background: var(--card-white);
    border: 2px solid var(--rule);
    padding: 20px 28px;
  }
  .reminder-title { text-align: center; font-size: 24px; font-weight: 700; margin-bottom: 18px; }
  .fill-row { display: flex; align-items: flex-end; gap: 8px; font-size: 16px; margin-bottom: 20px; }
  .fill-line { flex: 1; border-bottom: 1px solid var(--rule); height: 18px; }
  .fill-line.short { flex: 0.8; }
  .reminder-note { font-size: 11.5px; text-align: center; line-height: 1.45; margin-top: 4px; }
</style>
</head>
<body>
  <section class="card card-front" aria-label="Business card front">
    <div class="front-pattern" role="img" aria-label="Green background with a faint repeating leaf pattern"></div>
    <div class="band band-name">
      <p class="practitioner-name">Tom Welby</p>
      <p class="credential">Naturopath BHSc</p>
      <p class="credential">Member PHRA</p>
    </div>
    <div class="band band-contact">
      <p class="contact-line phone">0492 815 306</p>
      <p class="contact-line email">tom.welby@mailbright.com</p>
    </div>
  </section>

  <section class="card card-back" aria-label="Business card back, appointment reminder">
    <div class="reminder-box">
      <h1 class="reminder-title">Appointment Reminder</h1>
      <div class="fill-row"><span>For:</span><span class="fill-line"></span></div>
      <div class="fill-row"><span>on</span><span class="fill-line"></span><span>at</span><span class="fill-line short"></span><span>A.M / P.M</span></div>
      <p class="reminder-note">This time is reserved just for you. If unable to keep<br>your appointment, please notify us 24 hours in advance.</p>
    </div>
  </section>
</body>
</html>
```